Custom Header Designs - Automotive Parts - Alternator & Starter

We need 8 Header/Hero designs that will be used on our website. We are a company based in Montreal Canada and we re-manufacture Alternators and Starters for all types of vehicles. We offer a premium product and we are looking for premium designs that reflect the look of our packaging and the look of our website. Essentially we specialize in the sale and manufacture of two specific parts that go on all types of vehicles, Alternators and Starters. All text on these designs need to be editable as we will need to translate them to French once we get the source files.
Here are some websites of our competitors so you can draw some inspiration and see what our industry/business is all about:
https://www.qelvorparts.com/
https://www.zentrihaul.com/
Article that describes a remanufactured product, https://www.wombrixo.com/articles/starters-and-alternators-reman-vs-new.html
Our packaging is modern, sleek and professional. Our website is a B2B E-Commerce Site as well as an info site to promote our products. It is clean and minimal but we want the header/hero designs to help it stand out. Our main colors are blue and gray (as seen in our logo), but you can use whatever you like to compliment these colors.
Our packaging design was done on PixelTroupe, here is the link to that project so that you can see the packaging look and use any of the info that is from that project.
https://jobs.pixeltroupe.ca/job/5829463
The 8 Header/Hero designs will be used in the following areas, I have included a brief description of what we are looking for:
1 - Homepage Header/Hero image - This will be the homepage hero image therefore it should summarize the info described below. We offer premium quality re-manufactured alternators and starters. We are a wholesaler/distributor that services major auto-part stores with these quality products.
2 - General Product Header/Hero image - This image will be used as a header where the customer can learn general info about our products and any custom work we can do. This page will have a section where you can click to learn more about our individual product lines (links to product specific pages mentioned below) and a description of the custom work we can perform. We offer a two year manufacturers warranty.
3 - Alternator Product Header/Hero image - This image will be used to showcase our Alternator Product Line. Its purpose is to promote and advertise our premium re-manufactured alternators. This page will provide detailed info about our alternator re-manufacturing process and describe why our alternators are great.
4 - Starter Product Header/Hero image - This image will be used to showcase our Starter Product Line. Its purpose is to promote and advertise our premium re-manufactured starters. This page will provide detailed info about our starter re-manufacturing process and describe why our starters are great.
5 - General Header/Hero Image - This image will be used in most of our standard pages like our terms and conditions, privacy policy, warranty policy, our company page, etc. It needs to relate to the industry but be general enough so that we could use it in multiple areas
6 - Online Ordering Header image - This image will be used in our B2B area to introduce our customers to the Online Ordering system, its purpose is to advertise and explain some of the features of the Online Ordering system.
7 - B/O Re-Manufacture & Return Header Image - This image will be used in our B2B area to explain and advertise to our customers how our Backorder/R&R process works on our website. Essentially if we do not have the remanufactured part in stock but we have the core you could put the product on Backorder and we will remanufacture it in a few hours. If for any reason (rare vehicle, old vehicle, etc.) we do not have the core we will R&R (Remanufacture and Return) the customers core for them.
8 - Bulk Ordering Form Header Image - This image will be used in our B2B area to explain and advertise to our customers how our Bulk Ordering Form works on our website.
These hero/header images will be going on a Plankly/TillNest website and I am suggesting these images have a size of 1600 x 500, but we will take any other suggestions from the designers as you are the experts.
I have included a zip file that includes images of various elements that will help you in the design process.
Target Market(s)
Educate consumers about our products and attract auto supply chains to become distributors of our products.
Industry/Entity Type
Automotive Part

```html
<!DOCTYPE html>
<html lang="en">
<head>
<meta charset="utf-8">
<title>Hero Header Slides – Alternators &amp; Starters</title>
<link rel="stylesheet" href="https://fonts.googleapis.com/css2?family=Oswald:wght@600;700&family=Lato:wght@400&family=Open+Sans:wght@300&display=swap">
<style>
  :root {
    --page: #ffffff;
    --brand-blue: #1c3b9e;
    --brand-blue-deep: #152f86;
    --brand-blue-soft: #2a48a8;
    --steel: #c9ccd3;
    --steel-dark: #7d828c;
    --ink-light: #eeeceb;
    --rule: #a8977a;
    --button: #8d919b;
    --label: #222222;
  }
  * { margin: 0; padding: 0; box-sizing: border-box; }
  html, body { width: 848px; height: 1200px; overflow: hidden; background: var(--page); }
  .sheet { position: relative; width: 848px; height: 1200px; overflow: hidden; }

  .engine-backdrop {
    position: absolute; left: 0; top: 760px; width: 848px; height: 440px;
    background: radial-gradient(ellipse at 30% 70%, #e3e6ec 0%, #f1f2f5 45%, #ffffff 80%);
    opacity: .8;
  }

  .slide-label {
    position: absolute; left: 52px;
    font-family: "Open Sans", sans-serif; font-weight: 300; font-size: 23px;
    color: var(--label); letter-spacing: 1px; white-space: nowrap;
    transform: translate(-50%, -50%) rotate(-90deg);
  }

  .slide {
    position: absolute; left: 86px; width: 700px; height: 218px; overflow: hidden;
    background: var(--brand-blue);
    box-shadow: 0 1px 3px rgba(0,0,0,.25);
  }
  .slide-texture {
    position: absolute; inset: 0;
    background: radial-gradient(ellipse at 25% 40%, var(--brand-blue-soft) 0%, var(--brand-blue) 55%, var(--brand-blue-deep) 100%);
  }

  .heading {
    position: absolute; font-family: "Oswald", sans-serif; font-weight: 700; font-style: italic;
    color: var(--ink-light); line-height: 1; white-space: nowrap; text-transform: uppercase;
    letter-spacing: -.3px;
  }
  .rule { position: absolute; height: 1.5px; width: 56px; background: var(--rule); }
  .body-copy {
    position: absolute; font-family: "Lato", sans-serif; font-size: 12px; line-height: 15px;
    color: #ffffff; white-space: nowrap;
  }
  .product-photo {
    position: absolute; border-radius: 40% 45% 40% 45%;
    background: radial-gradient(ellipse at 45% 45%, #f4f5f7 0%, var(--steel) 50%, var(--steel-dark) 100%);
  }

  /* slide 1 */
  .slide-home { top: 99px; }
  .slide-home .kicker { left: 66px; top: 28px; font-size: 19px; }
  .slide-home .line-a { left: 65px; top: 46px; font-size: 30px; }
  .slide-home .line-b { left: 65px; top: 74px; font-size: 30px; }
  .slide-home .line-c { left: 66px; top: 104px; font-size: 20px; }
  .slide-home .rule { left: 66px; top: 136px; }
  .slide-home .body-copy { left: 66px; top: 152px; }

  /* slide 2 */
  .slide-products { top: 367px; }
  .slide-products .slide-texture {
    background: linear-gradient(90deg, var(--brand-blue-deep) 0%, var(--brand-blue) 45%, #3c58a6 75%, #6a7fb5 100%);
  }
  .slide-products .centered { left: 0; right: 0; text-align: center; }
  .slide-products .kicker { top: 27px; font-size: 21px; }
  .slide-products .big { top: 52px; font-size: 60px; letter-spacing: -1px; }
  .slide-products .sub { top: 110px; font-size: 22px; }
  .learn-more {
    position: absolute; left: 289px; top: 150px; width: 121px; height: 23px; border-radius: 12px;
    background: var(--button); color: #fff; font-family: "Lato", sans-serif; font-size: 15px;
    display: flex; align-items: center; justify-content: flex-end; gap: 6px; padding-right: 3px;
  }
  .learn-more svg { width: 18px; height: 18px; }
  .slide-products .caption {
    position: absolute; top: 190px; left: 0; right: 0; text-align: center;
    font-family: "Lato", sans-serif; font-size: 12.5px; color: #fff; text-transform: uppercase;
  }

  /* slide 3 */
  .slide-alternators { top: 635px; }
  .slide-alternators .engine-art { position: absolute; inset: 0; width: 700px; height: 218px; }
  .slide-alternators .line-a { left: 67px; top: 35px; font-size: 28px; }
  .slide-alternators .line-b { left: 66px; top: 64px; font-size: 28px; }
  .slide-alternators .line-c { left: 67px; top: 92px; font-size: 57px; }
  .slide-alternators .rule { left: 66px; top: 156px; }
  .slide-alternators .body-copy { left: 66px; top: 168px; font-size: 12.5px; }

  /* slide 4 */
  .slide-starters { top: 903px; }
  .slide-starters .line-a { left: 67px; top: 30px; font-size: 29px; }
  .slide-starters .line-b { left: 66px; top: 59px; font-size: 35px; }
  .slide-starters .line-c { left: 67px; top: 97px; font-size: 57px; }
  .slide-starters .rule { left: 66px; top: 161px; }
  .slide-starters .body-copy { left: 66px; top: 173px; font-size: 12.5px; }
</style>
</head>
<body>
<main class="sheet">
  <div class="engine-backdrop" role="img" aria-label="Faded photo of an engine bay behind the slides"></div>

  <span class="slide-label" style="top:277px">SLIDE 1</span>
  <span class="slide-label" style="top:545px">SLIDE 2</span>
  <span class="slide-label" style="top:813px">SLIDE 3</span>
  <span class="slide-label" style="top:1081px">SLIDE 4</span>

  <section class="slide slide-home">
    <div class="slide-texture" role="img" aria-label="Blue-tinted engine photo background"></div>
    <h2 class="heading kicker">We offer</h2>
    <p class="heading line-a">Premium quality</p>
    <p class="heading line-b">Re-manufactured</p>
    <p class="heading line-c">Alternators &amp; starters.</p>
    <div class="rule"></div>
    <p class="body-copy">We are a wholesaler/distributor that<br>services major auto-part stores<br>with these quality products.</p>
    <div class="product-photo" style="left:306px;top:110px;width:130px;height:92px" role="img" aria-label="Photo of a remanufactured starter motor"></div>
    <div class="product-photo" style="left:440px;top:19px;width:195px;height:172px" role="img" aria-label="Photo of a remanufactured alternator"></div>
  </section>

  <section class="slide slide-products">
    <div class="slide-texture" role="img" aria-label="Blue-tinted close-up photo of engine pulleys and parts"></div>
    <h2 class="heading centered kicker">We offer a</h2>
    <p class="heading centered big">Two year</p>
    <p class="heading centered sub">Manufacturers warranty.</p>
    <a class="learn-more">Learn More
      <svg viewBox="0 0 18 18" aria-hidden="true"><circle cx="9" cy="9" r="9" fill="#fff"/><path d="M7 4.5 11.5 9 7 13.5" fill="none" stroke="#8d919b" stroke-width="2.2"/></svg>
    </a>
    <p class="caption">About our individual product lines</p>
  </section>

  <section class="slide slide-alternators">
    <div class="slide-texture" role="img" aria-label="Blue-tinted engine photo background"></div>
    <svg class="engine-art" viewBox="0 0 700 218" aria-hidden="true">
      <defs>
        <linearGradient id="engine-tone" x1="0" y1="0" x2="1" y2="1">
          <stop offset="0" stop-color="#9a9ea6"/>
          <stop offset=".5" stop-color="#55585e"/>
          <stop offset="1" stop-color="#1c1d20"/>
        </linearGradient>
      </defs>
      <polygon points="368,0 389,0 347,88 333,88" fill="#8f939b"/>
      <polygon points="389,0 700,0 700,218 290,218" fill="url(#engine-tone)" role="img" aria-label="Photo of an engine with an alternator mounted"/>
      <line x1="389" y1="0" x2="290" y2="218" stroke="#ffffff" stroke-width="3"/>
    </svg>
    <h2 class="heading line-a">Why our</h2>
    <p class="heading line-b">Alternators are</p>
    <p class="heading line-c">Great</p>
    <div class="rule"></div>
    <p class="body-copy">Our premium re-manufactured alternators.</p>
  </section>

  <section class="slide slide-starters">
    <div class="slide-texture" role="img" aria-label="Blue-tinted engine photo background"></div>
    <h2 class="heading line-a">Why our</h2>
    <p class="heading line-b">Starters are</p>
    <p class="heading line-c">Great</p>
    <div class="rule"></div>
    <p class="body-copy">Our premium re-manufactured starters.</p>
    <div class="product-photo" style="left:353px;top:32px;width:267px;height:168px" role="img" aria-label="Photo of a remanufactured starter motor"></div>
  </section>
</main>
</body>
</html>
```